We sell companies excess stock for them

We need a business card for a company based in New Zealand called 'ShelfLark'.

Check out our website to get an idea www.shelflark.example

We help other businesses to;
- Sell Excess Stock
- Manage Product Returns
- Sell Company Assets

Our logo is attached for your reference
The font used is 'RifficFree-Bold'

Target Market(s)

Businesses

Industry/Entity Type

Business

Contact Information for Business Card

Name: Mara Quillby
Phone: 027 864 3190
email: maraquillby@shelflark.example
website: www.shelflark.example

Font styles to use
Other font styles liked:

Colors
9bcb3b

Requirements
Must have
Nice to have
Should not have

```html
<!DOCTYPE html>
<html lang="en">
<head>
<meta charset="utf-8">
<title>ShelfLark Business Card</title>
<link rel="stylesheet" href="https://fonts.googleapis.com/css2?family=Fredoka:wght@600;700&family=Roboto:wght@400&display=swap">
<style>
  :root {
    --backdrop: #3a3a3a;
    --card: #232323;
    --lime: #8fc31f;
    --white: #ffffff;
    --muted: #d9d9d9;
    --ink: #1d1d1d;
  }
  * { margin: 0; padding: 0; box-sizing: border-box; }
  html, body { width: 799px; height: 1200px; overflow: hidden; }
  body {
    background: var(--backdrop);
    font-family: "Roboto", Arial, sans-serif;
    position: relative;
  }
  .card {
    position: absolute;
    top: 294px;
    width: 350px;
    height: 612px;
    background: var(--card);
    overflow: hidden;
    box-shadow: 0 10px 30px rgba(0,0,0,.45);
  }
  .card--front { left: 33px; }
  .card--back { left: 416px; }

  .mascot {
    position: absolute;
    left: 50%;
    transform: translateX(-50%);
    border-radius: 40px;
    background: radial-gradient(circle at 45% 40%, #f39a1e 0 28%, #5fb82a 29% 62%, #ffffff 63% 75%, #2b2b2b 76%);
  }
  .card--front .mascot { top: 105px; width: 170px; height: 150px; }
  .card--back .mascot { top: 40px; width: 150px; height: 130px; }

  .wordmark {
    position: absolute;
    left: 0; right: 0;
    text-align: center;
    font-family: "Fredoka", sans-serif;
    font-weight: 700;
    color: var(--white);
    letter-spacing: -0.5px;
  }
  .card--front .wordmark { top: 268px; font-size: 48px; }
  .card--back .wordmark { top: 180px; font-size: 42px; }

  .rule {
    position: absolute;
    left: 40px; right: 40px;
    height: 1.5px;
    background: var(--lime);
  }
  .card--front .rule { top: 360px; }
  .card--back .rule { top: 242px; }

  .services {
    list-style: none;
    font-size: 17px;
    line-height: 22px;
  }
  .card--front .services {
    position: absolute;
    top: 385px; left: 95px;
    color: var(--white);
  }

  .person {
    position: absolute;
    top: 256px; left: 0; right: 0;
    text-align: center;
    color: var(--white);
  }
  .person__name {
    font-family: "Fredoka", sans-serif;
    font-weight: 700;
    font-size: 23px;
  }
  .person__title {
    font-size: 11px;
    color: var(--muted);
    border-left: 1px solid var(--lime);
    padding-left: 6px;
    margin-left: 4px;
    vertical-align: 3px;
  }
  .contact-icons {
    position: absolute;
    top: 300px; left: 0; right: 0;
    display: flex;
    justify-content: center;
    gap: 8px;
  }
  .contact-list {
    position: absolute;
    top: 320px; left: 0; right: 0;
    list-style: none;
    text-align: center;
    color: var(--white);
    font-size: 14px;
    line-height: 20px;
  }
  .band {
    position: absolute;
    left: 0; right: 0; bottom: 0;
    height: 185px;
    background: var(--lime);
  }
  .band .services {
    position: absolute;
    top: 62px; left: 95px;
    color: var(--ink);
  }
</style>
</head>
<body>
  <section class="card card--front">
    <div class="mascot" role="img" aria-label="Brand mascot illustration: running courier in green cap carrying an orange parcel"></div>
    <div class="wordmark">ShelfLark</div>
    <div class="rule"></div>
    <ul class="services">
      <li>Sell Excess Stock</li>
      <li>Manage Product Returns</li>
      <li>Sell Company Assets</li>
    </ul>
  </section>

  <section class="card card--back">
    <div class="mascot" role="img" aria-label="Brand mascot illustration: running courier in green cap carrying an orange parcel"></div>
    <div class="wordmark">ShelfLark</div>
    <div class="rule"></div>
    <div class="person">
      <span class="person__name">Mara Quillby</span><span class="person__title">Managing Director</span>
    </div>
    <div class="contact-icons">
      <svg width="11" height="11" viewBox="0 0 12 12" aria-label="Phone"><path d="M3 1h2l1 3-1.5 1a6 6 0 0 0 2.5 2.5L8 6l3 1v2a2 2 0 0 1-2 2A8 8 0 0 1 1 3a2 2 0 0 1 2-2z" fill="#8fc31f"/></svg>
      <svg width="12" height="11" viewBox="0 0 12 10" aria-label="Email"><rect x="0.5" y="0.5" width="11" height="9" fill="#8fc31f"/><path d="M0.5 0.5 6 5.5 11.5 0.5" stroke="#232323" fill="none"/></svg>
      <svg width="11" height="11" viewBox="0 0 12 12" aria-label="Website"><circle cx="6" cy="6" r="5.5" fill="#8fc31f"/><path d="M0.5 6h11M6 0.5c-3 3-3 8 0 11M6 0.5c3 3 3 8 0 11" stroke="#232323" stroke-width=".8" fill="none"/></svg>
    </div>
    <ul class="contact-list">
      <li>027 864 3190</li>
      <li>maraquillby@shelflark.example</li>
      <li>www.shelflark.example</li>
    </ul>
    <div class="band">
      <ul class="services">
        <li>Sell Excess Stock</li>
        <li>Manage Product Returns</li>
        <li>Sell Company Assets</li>
      </ul>
    </div>
  </section>
</body>
</html>
```